Flask Comet business cards + chance to win packaging and other design projects

including logo already designed.

******** I need 2 business cards:
1. that is general for the company
2. that is specific for me

*********On the reverse side of the business card I want it to be divided into 4 boxes and each box to describe a stage in how to use the product. I need the boxes to be numbered and the contents to be easy to absorb and include graphics showing the actions also.
Turning then photo's into simplified, cool illustrations** would be really cool. This would allow changes, like writing "water" on the bottle etc etc. Maybe have a fftness lady drinking at the end? Imagination over to you.
The photo's are of the prototype so the illustrations can replace the grey caps with bright orange etc etc

CAPTIONS FOR ILLUSTRATIONS
1. Charge the Flask Comet
2.The Flask Comet is now ready for making a shake anywhere, anytime !
3. Choose any bottled water or beverage, release shot cap and Jet powder in.
4. Shake bottle, enjoy!

Can you illustrate?
I just changed the photos and captions to simplify.
Please re read the brief, thanks

Target Market(s)

Fitness, weight loss, health
male and female
any potential powdered drink user.

quince, skyvale design style ? Clean, simple, bold, clever, cool

Industry/Entity Type

Business

Requirements
Must have
• Must have logo and flaskcomet.example

Card 1: email: info@flaskcomet.example

Card 2: Miles Thornbury LL.b. /President/ email:miles@flaskcomet.example/ office: 555 013 8841/ direct: 555 019 3627

I want the card to have a white background, not color blocked in.

I have included photos of the type of illustrations needed in each box.
In the illustrations pls make the flask comet army green and the caps bright orange.
Get the point across as simply as you can. Make it cool pls :)

```html
<!DOCTYPE html>
<html lang="en">
<head>
<meta charset="utf-8">
<title>Flask Comet Business Cards</title>
<link href="https://fonts.googleapis.com/css2?family=Arimo:wght@400;700&family=Passion+One:wght@400;700&display=swap" rel="stylesheet">
<style>
  :root {
    --page: #e9e6e1;
    --card: #ffffff;
    --orange: #ee7d2b;
    --navy: #2a2f6b;
    --ink: #1f1f1f;
    --magenta: #c0379b;
    --sky: #6fb7e0;
    --lime: #a8d04a;
    --amber: #ee8a34;
    --khaki-a: #8d8f5e;
    --khaki-b: #e8cdb2;
    --shadow: rgba(0,0,0,.18);
  }
  * { box-sizing: border-box; margin: 0; padding: 0; }
  html, body { width: 1200px; height: 1000px; overflow: hidden; }
  body {
    position: relative;
    background: var(--page);
    font-family: "Arimo", Arial, sans-serif;
    color: var(--ink);
  }
  .card {
    position: absolute;
    width: 520px;
    height: 297px;
    background: var(--card);
    box-shadow: 0 6px 18px var(--shadow);
    overflow: hidden;
  }

  /* ---------- Reverse: how-to steps ---------- */
  .card--steps { left: 50px; top: 70px; display: flex; }
  .step { position: relative; flex: 1; display: flex; flex-direction: column; }
  .step__art {
    margin: 14px 10px 0;
    height: 108px;
    border: 2px solid var(--orange);
  }
  .step:nth-child(1) .step__art { background: linear-gradient(160deg, var(--khaki-b), var(--khaki-a)); }
  .step:nth-child(2) .step__art { background: linear-gradient(200deg, var(--khaki-b), var(--khaki-a)); }
  .step:nth-child(3) .step__art { background: linear-gradient(180deg, #cfd6dc, var(--khaki-a)); }
  .step:nth-child(4) .step__art { background: linear-gradient(180deg, var(--khaki-b), #7ea36a); }
  .step__caption {
    flex: 1;
    margin: 8px 10px 0;
    font-family: "Passion One", Impact, sans-serif;
    color: var(--orange);
    line-height: 1.05;
  }
  .step__title { font-size: 17px; text-transform: uppercase; }
  .step__note { font-family: "Arimo", Arial, sans-serif; font-size: 9px; font-weight: 700; line-height: 1.25; margin-top: 2px; }
  .step__band {
    height: 74px;
    display: flex;
    align-items: center;
    justify-content: center;
    font-family: "Arimo", Arial, sans-serif;
    font-weight: 700;
    font-size: 30px;
    color: #fff;
  }
  .step:nth-child(1) .step__band { background: var(--magenta); }
  .step:nth-child(2) .step__band { background: var(--sky); }
  .step:nth-child(3) .step__band { background: var(--lime); }
  .step:nth-child(4) .step__band { background: var(--amber); }

  /* ---------- Brand name ---------- */
  .brand {
    display: flex;
    align-items: center;
    gap: 8px;
    font-family: "Arimo", Arial, sans-serif;
    font-weight: 700;
    color: var(--orange);
    text-transform: uppercase;
    white-space: nowrap;
  }
  .brand__dot { width: 14px; height: 14px; border-radius: 50%; background: var(--orange); flex: none; }

  /* ---------- Personal card ---------- */
  .card--personal { left: 630px; top: 70px; }
  .card--personal .rule-top {
    position: absolute; left: 262px; top: 22px; width: 238px; height: 1px; background: var(--navy);
  }
  .card--personal .rule-side {
    position: absolute; left: 262px; top: 22px; width: 1px; height: 275px; background: var(--navy);
  }
  .card--personal .brand { position: absolute; left: 20px; top: 190px; font-size: 24px; letter-spacing: 0; }
  .person { position: absolute; left: 278px; top: 40px; }
  .person__name { font-size: 15px; font-weight: 700; color: var(--orange); }
  .person__role { font-size: 13px; color: var(--navy); margin-top: 3px; }
  .contacts { list-style: none; margin-top: 22px; }
  .contacts li {
    display: flex; align-items: center; gap: 9px;
    font-size: 12px; font-weight: 700; color: var(--ink);
    margin-bottom: 7px;
  }
  .icon { width: 13px; height: 13px; flex: none; }

  /* ---------- General card ---------- */
  .card--general { left: 340px; top: 580px; }
  .card--general .brand { position: absolute; left: 34px; top: 190px; font-size: 34px; letter-spacing: 1px; }
  .card--general .contacts { position: absolute; right: 34px; top: 90px; margin: 0; }
  .card--general .contacts li { color: var(--orange); font-size: 13px; text-transform: uppercase; }
</style>
</head>
<body>

  <!-- Reverse side: four usage steps -->
  <section class="card card--steps" aria-label="How to use Flask Comet">
    <div class="step">
      <div class="step__art" role="img" aria-label="Illustration: hand loading powder into the green Flask Comet with an orange cap"></div>
      <div class="step__caption"><p class="step__title">Charge the Flask Comet</p></div>
      <div class="step__band">1</div>
    </div>
    <div class="step">
      <div class="step__art" role="img" aria-label="Illustration: hand holding the charged Flask Comet"></div>
      <div class="step__caption">
        <p class="step__title">The Flask Comet</p>
        <p class="step__note">is now ready for making a shake anywhere, anytime!</p>
      </div>
      <div class="step__band">2</div>
    </div>
    <div class="step">
      <div class="step__art" role="img" aria-label="Illustration: Flask Comet releasing powder into a water bottle"></div>
      <div class="step__caption">
        <p class="step__note">Choose any bottled water or beverage, release shot cap and</p>
        <p class="step__title">Jet powder in.</p>
      </div>
      <div class="step__band">3</div>
    </div>
    <div class="step">
      <div class="step__art" role="img" aria-label="Illustration: person drinking the shake from the bottle"></div>
      <div class="step__caption"><p class="step__title">Shake bottle. Enjoy!</p></div>
      <div class="step__band">4</div>
    </div>
  </section>

  <!-- Personal card -->
  <section class="card card--personal" aria-label="Personal business card">
    <span class="rule-top"></span>
    <span class="rule-side"></span>
    <div class="brand"><span class="brand__dot"></span>Flask Comet</div>
    <div class="person">
      <p class="person__name">Miles Thornbury LL.b.</p>
      <p class="person__role">President</p>
      <ul class="contacts">
        <li>
          <svg class="icon" viewBox="0 0 16 16"><path fill="#2a2f6b" d="M3 1h3l1.5 4-2 1.3a9 9 0 0 0 4.2 4.2L11 8.5l4 1.5v3a2 2 0 0 1-2 2A12 12 0 0 1 1 3a2 2 0 0 1 2-2z"/></svg>
          555 013 8841
        </li>
        <li>
          <svg class="icon" viewBox="0 0 16 16"><rect x="4" y="1" width="8" height="14" rx="1.5" fill="none" stroke="#2a2f6b" stroke-width="1.6"/><circle cx="8" cy="12.5" r="1" fill="#2a2f6b"/></svg>
          555 019 3627
        </li>
        <li>
          <svg class="icon" viewBox="0 0 16 16"><rect x="1" y="3" width="14" height="10" fill="#2a2f6b"/><path d="M1.5 3.5 8 9l6.5-5.5" fill="none" stroke="#fff" stroke-width="1.2"/></svg>
          miles@flaskcomet.example
        </li>
        <li>
          <svg class="icon" viewBox="0 0 16 16"><circle cx="8" cy="8" r="7" fill="#2a2f6b"/><path d="M1 8h14M8 1c-3 3.5-3 10.5 0 14M8 1c3 3.5 3 10.5 0 14" fill="none" stroke="#fff" stroke-width="1"/></svg>
          www.flaskcomet.example
        </li>
      </ul>
    </div>
  </section>

  <!-- General company card -->
  <section class="card card--general" aria-label="Company business card">
    <div class="brand"><span class="brand__dot"></span>Flask Comet</div>
    <ul class="contacts">
      <li>
        <svg class="icon" viewBox="0 0 16 16"><circle cx="8" cy="8" r="7" fill="#2a2f6b"/><path d="M1 8h14M8 1c-3 3.5-3 10.5 0 14M8 1c3 3.5 3 10.5 0 14" fill="none" stroke="#fff" stroke-width="1"/></svg>
        www.flaskcomet.example
      </li>
      <li>
        <svg class="icon" viewBox="0 0 16 16"><rect x="1" y="3" width="14" height="10" fill="#2a2f6b"/><path d="M1.5 3.5 8 9l6.5-5.5" fill="none" stroke="#fff" stroke-width="1.2"/></svg>
        info@flaskcomet.example
      </li>
    </ul>
  </section>

</body>
</html>
```